Stationery Design Project

We need a stationery design for a new business consulting business based in New Zealand.
We have the logo and business cards designed and we're looking for letterhead, compliments slip and PowerPoint presentation format that aligns with our business cards.
Industry/Entity Type
Business
Requirements
Must have
- same colors and format as business cards

```html
<!DOCTYPE html>
<html lang="en">
<head>
<meta charset="utf-8">
<title>Kestrel Consulting – Stationery</title>
<link rel="stylesheet" href="https://fonts.googleapis.com/css2?family=Poppins:wght@400;600&family=Arimo:wght@400;700&display=swap">
<style>
  :root {
    --green: #8cc63f;
    --grey-band: #a7a9ac;
    --grey-bar: #8e8f91;
    --grey-text: #9a9a9a;
    --ink: #6d6e71;
    --paper: #ffffff;
    --stage: #ebebeb;
  }
  * { margin: 0; padding: 0; box-sizing: border-box; }
  html, body { width: 1200px; height: 877px; overflow: hidden; }
  body {
    background: var(--stage);
    font-family: "Arimo", Arial, sans-serif;
    position: relative;
  }

  /* Cover sheet */
  .cover {
    position: absolute; left: 52px; top: 99px; width: 528px; height: 745px;
    background: radial-gradient(ellipse at 50% 40%, #ffffff 0%, #f1f1f1 55%, #dcdcdc 100%);
    box-shadow: 0 2px 6px rgba(0,0,0,.12);
    overflow: hidden;
  }
  .cover__top-green { position: absolute; left: 0; top: 0; width: 100%; height: 12px; background: var(--green); }
  .cover__top-grey { position: absolute; left: 0; top: 12px; width: 100%; height: 30px; background: var(--grey-band); }
  .cover__logo { position: absolute; left: 100px; top: 168px; display: flex; align-items: center; gap: 18px; }
  .brand-square { width: 46px; height: 46px; background: var(--green); flex: none; }
  .cover__name {
    font-family: "Poppins", sans-serif; font-weight: 600; color: var(--green);
    line-height: 1;
  }
  .cover__name .word-main { display: block; font-size: 68px; letter-spacing: -1px; }
  .cover__name .word-sub { display: block; font-size: 26px; text-align: right; margin-top: 4px; }
  .cover__mark-faint {
    position: absolute; left: 140px; top: 430px; width: 110px; height: 110px;
    background: #e4e4e4;
  }
  .cover__bottom-grey { position: absolute; left: 0; bottom: 36px; width: 100%; height: 9px; background: var(--grey-band); }
  .cover__bottom-green {
    position: absolute; left: 0; bottom: 0; width: 100%; height: 36px; background: var(--green);
    color: #fff; font-family: "Poppins", sans-serif; font-size: 17px; letter-spacing: .5px;
    display: flex; align-items: center; justify-content: center;
  }

  /* Letterhead */
  .letterhead {
    position: absolute; left: 613px; top: 99px; width: 523px; height: 745px;
    background: var(--paper);
    box-shadow: 0 2px 6px rgba(0,0,0,.12);
  }
  .letterhead__top-green { position: absolute; right: 0; top: 0; width: 193px; height: 14px; background: var(--green); }
  .letterhead__logo {
    position: absolute; left: 72px; top: 54px; display: flex; align-items: center; gap: 7px;
    font-family: "Poppins", sans-serif; font-weight: 600; color: var(--green); font-size: 21px;
    white-space: nowrap;
  }
  .letterhead__logo .brand-square { width: 13px; height: 13px; }
  .contact { position: absolute; left: 334px; top: 20px; font-size: 7.5px; line-height: 10.5px; color: var(--ink); white-space: nowrap; }
  .contact__role { font-family: "Poppins", sans-serif; font-weight: 600; color: var(--green); font-size: 10px; line-height: 13px; }
  .contact__dot { display: inline-block; width: 5px; height: 5px; border-radius: 50%; background: var(--green); margin-right: 3px; }
  .letterhead__side-bar { position: absolute; left: -3px; top: 184px; width: 22px; height: 490px; background: var(--grey-bar); }

  .letter { position: absolute; left: 54px; top: 186px; width: 420px; font-size: 9px; line-height: 14px; color: var(--grey-text); }
  .letter__date { text-align: right; margin-bottom: 22px; }
  .letter p { margin-bottom: 16px; text-align: justify; }
  .letter__signature { width: 60px; height: 18px; border-bottom: 1px solid #c8c8c8; margin: 10px 0 10px; }
</style>
</head>
<body>

  <section class="cover">
    <div class="cover__top-green"></div>
    <div class="cover__top-grey"></div>
    <div class="cover__logo">
      <span class="brand-square"></span>
      <div class="cover__name">
        <span class="word-main">Kestrel</span>
        <span class="word-sub">Consulting</span>
      </div>
    </div>
    <div class="cover__mark-faint"></div>
    <div class="cover__bottom-grey"></div>
    <div class="cover__bottom-green">www.kestrelconsulting.com</div>
  </section>

  <section class="letterhead">
    <div class="letterhead__top-green"></div>
    <div class="letterhead__logo"><span class="brand-square"></span>Kestrel Consulting</div>
    <div class="contact">
      <div class="contact__role">CONSULTANT NAME</div>
      <div>Kestrel Consulting</div>
      <div>PO Box 2290</div>
      <div>Marlow Bay 4410 Eastvale</div>
      <div>T. +00 4 555 0172</div>
      <div><span class="contact__dot"></span>info@kestrelconsulting.com</div>
      <div><span class="contact__dot"></span>www.kestrelconsulting.com</div>
    </div>
    <div class="letterhead__side-bar"></div>

    <div class="letter">
      <div class="letter__date">14 March 2024</div>
      <p>Dear Ms Harper,</p>
      <p>Thank you for meeting with our team last week to discuss your growth plans for the coming year. We have reviewed the notes from our session and prepared a short outline of the areas where we believe our advice can add the most value to your business operations and staff.</p>
      <p>The first stage covers a review of current processes, finances and reporting. The second stage sets clear targets with your leadership group, and the final stage supports the rollout with regular check-ins. Each stage ends with a written summary and agreed next steps for your team to follow.</p>
      <p>Please let us know a suitable time to confirm the proposal. We look forward to working with you.</p>
      <div>Kind regards,</div>
      <div class="letter__signature"></div>
      <div>Daniel Reeve</div>
      <div>Senior Consultant</div>
    </div>
  </section>

</body>
</html>
```